Fun Language School in San Diego, CA - We want cool Business Card

We need a new business card design for our new logo. We are a language school in beautiful San Diego, California. Our target is students from all over the world who age from 18 to 25. They come to our school to learn English. Our school has a modern look, trending and fun place. We are the only language school who use tablets in class. We are student oriented, Students Come First is our slogan. We are re-branding ourselves with a new logo. We would like to see a designs that use our new logo and it should reflect the feel of young, fun, modern, high-tech and attractive to young people.
I've seen some business card designs with transparent look, unusual shapes, we are open to any cool ideas. Thank you very much!

In order for you to know more about our school, here are the links to our Youtube Channel and Facebook.

Youtube: https://www.vidloop.example/channel/ZXpo84kR-21bvn5wQ7t2LmHd
Facebook: https://www.friendspace.example/TVSchool

Target Market(s)

Our target is students from all over the world who age from 18 to 25. International students.

Industry/Entity Type

School

Font styles to use
Sans Serif

Requirements
Must have
• Our new logo. Name, title and address.
Should not have
• Other colors other than the ones we have in our logo. Characters are fine.

```html
<!DOCTYPE html>
<html lang="en">
<head>
<meta charset="utf-8">
<title>Tidewave School – Business Card</title>
<link rel="stylesheet" href="https://fonts.googleapis.com/css2?family=Arimo:wght@400;700&display=swap">
<style>
  :root {
    --backdrop: #e0060f;
    --ink: #0b0b0d;
    --teal: #00a6b3;
    --lime: #bae639;
    --white: #ffffff;
    --text: #111111;
  }
  * { margin: 0; padding: 0; box-sizing: border-box; }
  html, body {
    width: 1200px;
    height: 1000px;
    overflow: hidden;
    background: var(--backdrop);
    font-family: "Arimo", Arial, sans-serif;
  }
  .card {
    position: absolute;
    left: 225px;
    top: 201px;
    width: 750px;
    height: 440px;
    background: var(--ink);
    border-radius: 0 0 0 100px;
    overflow: hidden;
    color: var(--text);
  }
  .card-shapes {
    position: absolute;
    inset: 0;
    width: 750px;
    height: 440px;
  }
  .holder {
    position: absolute;
    left: 30px;
    top: 26px;
    line-height: 1.3;
  }
  .holder-name { font-size: 23px; font-weight: 400; }
  .holder-name strong { font-weight: 700; }
  .holder-title { font-size: 20px; }
  .brand-name {
    position: absolute;
    left: 430px;
    top: 185px;
    transform: translate(-50%, -50%) rotate(-30deg);
    white-space: nowrap;
    color: var(--white);
    font-size: 58px;
    font-weight: 400;
    letter-spacing: 1px;
  }
  .contact {
    position: absolute;
    right: 25px;
    top: 263px;
    text-align: right;
    font-size: 21px;
    line-height: 28px;
  }
  .contact .address { margin-bottom: 7px; }
  .contact .lines p { line-height: 31px; }
</style>
</head>
<body>
  <div class="card">
    <svg class="card-shapes" viewBox="0 0 750 440" aria-hidden="true">
      <polygon class="band-teal" points="0,0 420,0 0,244" fill="var(--teal)"/>
      <polygon class="band-lime" points="750,109 750,440 175,440" fill="var(--lime)"/>
      <circle class="brand-dot" cx="120" cy="326" r="88" fill="var(--teal)"/>
    </svg>

    <div class="holder">
      <p class="holder-name">Marcus <strong>Reed</strong></p>
      <p class="holder-title">Principle</p>
    </div>

    <p class="brand-name">Tidewave School</p>

    <div class="contact">
      <div class="address">
        <p>2480 Harbor Ave, Ste 210</p>
        <p>San Diego, CA 92110</p>
      </div>
      <div class="lines">
        <p>P: +1.619.555.0148</p>
        <p>F: 619.555.0193</p>
        <p>E: hello@tidewave.example</p>
      </div>
    </div>
  </div>
</body>
</html>
```